New Business Card Design Project

Hi! I would like for you to design a business card for our aesthetic injections business. We offer Zelvia, filler, skin care. I would like it to be elegant, feminine, modern and sleek/clean. I like black/gold foil/ivory/parchment colors. It can be either one or two sided. I would like matte black with gold foil logo on one side and ivory with gold foil information on the other side

Target Market(s)

target market is the discerning woman who wants to look her best

Industry/Entity Type

beauty

Contact Information for Business Card

logo, name, phone, email, website, instagram, facebook, location

Requirements
Must have
• logo and info
Nice to have
• the icons for cell, instagram, email, fb etc
Should not have
• images of people

```html
<!DOCTYPE html>
<html lang="en">
<head>
<meta charset="utf-8">
<title>Maison Velour – Business Card</title>
<link rel="stylesheet" href="https://fonts.googleapis.com/css2?family=Cinzel:wght@500&family=Montserrat:wght@300;400;500&display=swap">
<style>
  :root {
    --backdrop: #9d9d9d;
    --ivory: #fbfaf7;
    --ink: #2b2b2b;
    --ink-soft: #5d5d5d;
    --rule: #7a7a7a;
    --matte-top: #3a3a3a;
    --matte-bottom: #161616;
    --foil: #f2f2f2;
  }
  * { box-sizing: border-box; margin: 0; padding: 0; }
  html, body { width: 1200px; height: 982px; overflow: hidden; }
  body {
    background: var(--backdrop);
    font-family: "Montserrat", sans-serif;
    display: flex;
    align-items: center;
    justify-content: center;
    gap: 60px;
  }
  .card {
    position: relative;
    width: 320px;
    height: 540px;
    box-shadow: 0 14px 30px rgba(0,0,0,0.28);
  }

  /* Front: ivory information side */
  .card--front {
    background: var(--ivory);
    color: var(--ink);
    text-align: center;
  }
  .brand {
    position: absolute;
    top: 84px;
    left: 0;
    right: 0;
  }
  .brand__name {
    font-weight: 400;
    font-size: 34px;
    letter-spacing: 1px;
    color: var(--ink);
  }
  .brand__sub {
    margin-top: 14px;
    font-size: 10px;
    letter-spacing: 12px;
    padding-left: 12px;
    color: var(--ink);
  }
  .person {
    position: absolute;
    top: 252px;
    left: 0;
    right: 0;
  }
  .person__name {
    font-family: "Cinzel", serif;
    font-weight: 500;
    font-size: 22px;
    letter-spacing: 1px;
    color: var(--ink);
  }
  .person__role {
    margin-top: 2px;
    font-size: 13px;
    font-weight: 400;
    color: var(--ink-soft);
  }
  .address {
    position: absolute;
    top: 326px;
    left: 0;
    right: 0;
    font-size: 12.5px;
    line-height: 1.45;
    color: var(--ink-soft);
    font-style: normal;
  }
  .contact {
    position: absolute;
    top: 384px;
    left: 0;
    right: 0;
    list-style: none;
    font-size: 12.5px;
    line-height: 1.5;
    color: var(--ink-soft);
  }
  .contact b { font-weight: 500; color: var(--ink); }
  .social {
    position: absolute;
    top: 474px;
    left: 0;
    right: 0;
    height: 20px;
    display: flex;
    align-items: center;
    gap: 6px;
  }
  .social__rule { flex: 1; height: 1px; background: var(--rule); }
  .social__dot {
    width: 18px;
    height: 18px;
    border-radius: 50%;
    background: var(--ink-soft);
  }
  .social__join { width: 6px; height: 1px; background: var(--rule); }
  .base-rule {
    position: absolute;
    left: 0;
    right: 0;
    bottom: 26px;
    height: 1px;
    background: var(--rule);
  }

  /* Back: matte black logo side */
  .card--back {
    background: linear-gradient(160deg, var(--matte-top), var(--matte-bottom) 70%);
  }
  .back__line {
    position: absolute;
    left: 50%;
    width: 1.5px;
    margin-left: -0.75px;
    background: var(--foil);
  }
  .back__line--top { top: 0; height: 130px; }
  .back__line--bottom { bottom: 0; height: 130px; }
  .seal {
    position: absolute;
    top: 165px;
    left: 50%;
    width: 210px;
    height: 210px;
    margin-left: -105px;
    border: 1.5px solid var(--foil);
    border-radius: 50%;
    display: flex;
    flex-direction: column;
    align-items: center;
    justify-content: center;
    color: var(--foil);
  }
  .seal__name {
    font-weight: 400;
    font-size: 26px;
    letter-spacing: 1px;
  }
  .seal__sub {
    margin-top: 10px;
    font-size: 9px;
    letter-spacing: 9px;
    padding-left: 9px;
  }
</style>
</head>
<body>
  <section class="card card--front" aria-label="Business card, information side">
    <div class="brand">
      <p class="brand__name">Maison Velour</p>
      <p class="brand__sub">LOUNGE</p>
    </div>
    <div class="person">
      <p class="person__name">MARLENA</p>
      <p class="person__role">Executive Director</p>
    </div>
    <address class="address">482 Alder Row Ste 210<br>Fairhaven OR 97000</address>
    <ul class="contact">
      <li><b>P:</b> (555) 014-2290</li>
      <li><b>E:</b> hello@maisonvelour.com</li>
      <li><b>W:</b> www.maisonvelour.com</li>
    </ul>
    <div class="social" aria-label="Social profiles">
      <span class="social__rule"></span>
      <span class="social__dot"></span>
      <span class="social__join"></span>
      <span class="social__dot"></span>
      <span class="social__rule"></span>
    </div>
    <div class="base-rule"></div>
  </section>

  <section class="card card--back" aria-label="Business card, logo side">
    <span class="back__line back__line--top"></span>
    <div class="seal">
      <p class="seal__name">Maison Velour</p>
      <p class="seal__sub">LOUNGE</p>
    </div>
    <span class="back__line back__line--bottom"></span>
  </section>
</body>
</html>
```